Design and put together a 5 page A4 brochure for a Training Programme

Carrowmere Institute of Training deliver a Nationally Accredited Programme in Medical Reception and Administration.

We have a new Qualification (Cert III Business Administration) and we require a 5 page brochure to be designed. (I have CHANGED THIS TO 5 Pages as I can see it is too crowded and not clean enough)

I would put a 6th page in as an application form.

We have recently rebranded our website which is currently under development - so a .jpg will be available of the 'look and feel of this'. I will also upload some stock photos which could be used in the design.

This is an important project for us - so your fantastic work will be greatly appreciated.

This project is fairly urgent - so it is likely we will be choosing a 'winner' to work with sooner rather than later.

Thanks for considering!

I will be uploading various graphics/drafts now.
Updates

Target Market(s)

1/ Women 25-45 yrs undertaking studies in being a medical receptionist
2/ Medical Practices who are hiring Trainees for their medical clinic or hospital

Industry/Entity Type

Medical

Font styles to use
Serif
Sans Serif

Colors
0455a3
fbe7d2
f68e4e
fef4ee
3176b5
33a6d7
f37122

Requirements
Must have
• Clear and clean design - professional
• Graphics of medical pictures (I will supply some so you get the look and feel of wht we are looking for)
• Corporate branding (I will upload a .jpg of new website design for look and feel
• The colour I would like with blue is also a STONE colour - I could not find it in the colour wheel on this site.
• The partner logos should be on the last page probably in one faded colour (such as grey)
Should not have
• I must be able to see the inside of the brochure also, I can not pick this purely on the front cover. Thanks :-)
• I have also now updated the Company Logo

```html
<!DOCTYPE html>
<html lang="en">
<head>
<meta charset="utf-8">
<title>Carrowmere Cert III Business Admin (Medical) – Programme Details</title>
<link href="https://fonts.googleapis.com/css2?family=Cabin:wght@400;500&family=Exo+2:wght@800&display=swap" rel="stylesheet">
<style>
  :root {
    --band: #2ea4dc;
    --heading: #0d2a5c;
    --body: #0f2748;
    --accent: #0455a3;
    --bg-centre: #ffffff;
    --bg-mid: #eaf5fc;
    --bg-edge: #cfe8f8;
  }
  html, body { margin: 0; padding: 0; overflow: hidden; }
  .page {
    position: relative;
    width: 849px;
    height: 1200px;
    overflow: hidden;
    background: radial-gradient(ellipse 75% 60% at 50% 50%, var(--bg-centre) 0%, var(--bg-mid) 55%, var(--bg-edge) 100%);
    font-family: "Cabin", sans-serif;
    color: var(--body);
  }
  .top-band {
    position: absolute; top: 0; left: 0; width: 100%; height: 16px;
    background: var(--band);
  }
  .section { position: absolute; left: 44px; width: 754px; }
  .section-title {
    font-family: "Exo 2", sans-serif;
    font-weight: 800;
    font-size: 16.5px;
    line-height: 22px;
    letter-spacing: 0.3px;
    color: var(--heading);
    margin: 0;
    padding-left: 6px;
  }
  .section-title.flush { padding-left: 0; }
  .section p {
    margin: 0 0 16.5px 0;
    font-size: 11.4px;
    line-height: 24px;
    text-align: justify;
  }
  .section p:last-child { margin-bottom: 0; }
  .section .duration {
    font-size: 11.5px;
    line-height: 22px;
    color: var(--accent);
    margin: 9px 0 6px 0;
    text-align: left;
  }
  .indent p { padding-left: 6px; }
</style>
</head>
<body>
<div class="page">
  <div class="top-band"></div>

  <section class="section" style="top:72px;">
    <h2 class="section-title">Unique Delivery Model – Combining face-to-face learning with self paced</h2>
    <div style="margin-top:25px;">
      <p>The Carrowmere Cert III Business Admin (Medical) Programme offers a unique structure to the medical administrative trainee - offering flexibility, intensive face-to-face training of crucial medical units combined with a self-paced home learning and a unique on-line learning programme. This allows studies to be undertaken at a convenient time by students and trainees.</p>
      <p>The programme will adjust to differing skill levels and ability to commit time to the programme and can be completed in as little as 6 months to a maximum of 12 months – depending on prior experience and skills.</p>
      <p>Carrowmere believe some units can only be taught effectively with face to face training led by industry experts and cannot be taught effectively by online learning alone. Therefore Carrowmere's Core Medical units are taught in workshop settings in 5 Saturdays (or through the week by prior arrangement) followed by self-paced and online delivery of core administration modules. The programme is further followed up with an intensive one day workshop.</p>
      <p>For Traineeships, our Trainers physically attend site 1-2 times for personalised mentoring. There is a mentor/trainer assessor available at all times during our programme for all students.</p>
      <p>All students are invited to Carrowmere's Computing Medical Software workshop day, where students work hands-on in a workplace simulated environment. &nbsp;Participants receive a complimentary demo copy of a Popular Medical software programme.</p>
    </div>
  </section>

  <section class="section" style="top:535px;">
    <h2 class="section-title flush">Combined Assessment Approach</h2>
    <p class="duration">Duration : &nbsp; 6 – 12 months</p>
    <p style="padding-left:2px;">Carrowmere utilise a variety of assessment processes which allow different learning styles to benefit from our programme. Assessment tools may include questioning, quizzes, assignments, projects, case studies and more. Workplace project work simulates real workplace activities utilising real medical forms, situations, case histories, resources, practice software and represents industry standards including RCGPA, NMA, the National Medical Practice Board, First Aid Alliance and the Cardiac Care Council.</p>
  </section>

  <section class="section indent" style="top:754px;">
    <h2 class="section-title">Student Support</h2>
    <div style="margin-top:12px;">
      <p>Students have direct access to a Trainer/Mentor for the duration of the programme and have direct access to Carrowmere Health Student On-Line Forum which students can engage with fellow students and trainers from across Australia.</p>
    </div>
  </section>

  <section class="section indent" style="top:912px;">
    <h2 class="section-title">Funding (Queensland)</h2>
    <div style="margin-top:17px;">
      <p>The Queensland Government will offset the cost of study for eligible students. &nbsp;You will still need to pay for a portion of your study costs. Carrowmere Institute of Training has been chosen by the Department of Education and Training to deliver Government Subsidised Courses through the Certificate 3 Guarantee programme, VET Investment Plan and User Choice initiatives. Therefore Carrowmere Institute are able to offer subsidised training for students who are eligible for the Certificate 3 Guarantee Programme, delivery and manage Traineeships in Cert III Business Administration (Medical) and offer services in Vocational Training &nbsp;r Schools (VET is) .For Course and funding opportunities, please contact our office by email or phone to find out more.</p>
    </div>
  </section>
</div>
</body>
</html>
```